Create the artwork for Velvetharbor's debut album, 'Where Rivers Bend Slowly'!

We are a cinematic pop/jazz quartet from Oslo/London looking for someone to create the artwork for our debutalbum, 'Where Rivers Bend Slowly'. This is a project we are incredibly proud of, and we are looking for the perfect artwork to complement our music.

We want the artwork to convey the organic feel of our sound, yet be eye-catching with bright colours. Attached are several examples for inspiration. The title of the album, 'Where Rivers Bend Slowly', should be an inspiration for the design in a subtle/abstract way. Think out of the box here, we are not looking for a hundred solar system designs.

You can find an album teaser here for inspiration: https://audiostreamhub.example/velvetharbormusic/album-teaser

This is our webpage: velvetharbormusic.example

Excited to see what you come up with and to work with some brilliant creatives !

Much love,

Velvetharbor
Updates

Everyone, thanks for your effort and great designs! We're discussing right now and will get back to you with feedback and suggested edits very shortly. Thanks for your patience! Much love, Velvetharbor

Requirements
Must have
• Ready-to-print high-res files in standard CD Cover format
• Artwork ready for digital release on tunewave, Songvault, and social media channels
Nice to have
• Would love to have smaller extensions of the artwork (pattern or pieces of art in same theme) to use on webpage/social media channels.

```html
<!DOCTYPE html>
<html lang="en">
<head>
<meta charset="utf-8">
<title>Velvetharbor – Where Rivers Bend Slowly</title>
<link rel="stylesheet" href="https://fonts.googleapis.com/css2?family=Cinzel:wght@400&family=Poiret+One&display=swap">
<style>
  :root {
    --sky-top: #c9dde0;
    --sky-mist: #e8f1f3;
    --haze-blue: #8fb3c9;
    --portal-violet: #7a63b8;
    --portal-core: #c9b6ec;
    --ground-sage: #b9bf9c;
    --ground-sand: #e8dfa8;
    --title-ink: #1d2a44;
    --name-ink: #55226f;
  }
  html, body {
    margin: 0;
    padding: 0;
    width: 1200px;
    height: 1200px;
    overflow: hidden;
    background: var(--sky-mist);
  }
  .album-cover {
    position: relative;
    width: 1200px;
    height: 1200px;
    overflow: hidden;
  }
  .cover-artwork {
    position: absolute;
    inset: 0;
    background:
      radial-gradient(ellipse 230px 210px at 600px 560px, var(--portal-core) 0%, var(--portal-violet) 45%, rgba(122, 99, 184, 0) 100%),
      radial-gradient(ellipse 420px 300px at 600px 330px, rgba(255, 255, 255, 0.85) 0%, rgba(255, 255, 255, 0) 100%),
      linear-gradient(180deg,
        var(--sky-top) 0%,
        var(--sky-mist) 22%,
        var(--haze-blue) 34%,
        var(--sky-mist) 46%,
        var(--haze-blue) 58%,
        var(--ground-sage) 70%,
        var(--ground-sand) 90%,
        var(--ground-sage) 100%);
  }
  .cover-type {
    position: absolute;
    inset: 0;
  }
  .album-title {
    font-family: "Poiret One", sans-serif;
    font-size: 50px;
    fill: var(--title-ink);
  }
  .artist-name {
    font-family: "Cinzel", serif;
    font-size: 112px;
    fill: var(--name-ink);
  }
</style>
</head>
<body>
  <main class="album-cover">
    <div class="cover-artwork" role="img" aria-label="Surreal symmetrical landscape: a glowing violet portal framed by pale stone spires, lightning and floating lights over a misty sandy plain"></div>
    <svg class="cover-type" width="1200" height="1200" viewBox="0 0 1200 1200">
      <text class="album-title" x="600" y="156" text-anchor="middle" textLength="700" lengthAdjust="spacingAndGlyphs">WHERE RIVERS BEND SLOWLY</text>
      <text class="artist-name" x="600" y="1117" text-anchor="middle" textLength="1160" lengthAdjust="spacingAndGlyphs">VELVETHARBOR</text>
    </svg>
  </main>
</body>
</html>
```